Marwood Holiday Jubilee 2025

We’re looking for a designer to help refresh the visual identity of our annual Christmas show while maintaining continuity from previous years. The updated design should feel festive, and warm, with a sense of celebration and anticipation. We’d like a central graphic that can be adapted for posters, social media, and digital signage, along with supporting assets for flyers and banners.

We’re open to seasonal color palettes such as rich reds, deep greens or blues, golds, silvers, or cool winter tones, and prefer typography that’s clear and elegant. The overall look should feel familiar to returning audiences while inviting and engaging for newcomers.

Two key groups: the current attenders of our congregation and the broader community in our suburb of Rochester, NY. Our congregation is made up of families, older adults, and young professionals who value faith, community and spiritual growth. The surrounding community is a fast growing friendly and family-oriented area of young professionals and longtime families.

We’re looking for a designer to help refresh the visual identity of our annual Christmas show while maintaining continuity with the theme and tone of previous years. The updated design should feel festive, and warm, with a sense of celebration and anticipation. We’d like a central graphic that can be adapted for posters, social media, and digital signage, along with supporting assets for flyers and banners.

Target Market(s)

Two key groups: the current attenders of our congregation and the broader community in our suburb of Rochester, NY. Our congregation is made up of families, older adults, and young professionals who value faith, community and spiritual growth. The surrounding community is a fast growing friendly and family-oriented area of young professionals and long time families.

Industry/Entity Type

Non-profit. Church

Font styles to use
Serif
Decorative
Script
Other font styles liked:
• Quentin

Requirements
Must have
• Sparkle, eye catching
Should not have
• must not look identical to the uploaded versions

```html
<!DOCTYPE html>
<html lang="en">
<head>
<meta charset="utf-8">
<title>Marwood Holiday Jubilee 2025 – Banner Set</title>
<link rel="stylesheet" href="https://fonts.googleapis.com/css2?family=Allura&family=Archivo+Black&family=Montserrat:wght@500&family=Pinyon+Script&display=swap">
<style>
  :root {
    --gold: #b8952c;
    --gold-light: #ead17a;
    --gold-dark: #8c6d18;
    --white: #ffffff;
    --copper: #c4602a;
    --copper-light: #ec9d62;
    --copper-dark: #9a4318;
    --plum: #221a34;
    --wine: #5b1a20;
    --rust: #7d3620;
    --glint: rgba(255,250,225,.95);
    --grain: rgba(70,45,5,.55);
    --star: #fff4d6;
  }
  * { box-sizing: border-box; margin: 0; padding: 0; }
  html, body { width: 711px; height: 1200px; overflow: hidden; background: var(--white); }
  .banner-set { width: 711px; height: 1200px; display: flex; flex-direction: column; }
  .banner { position: relative; width: 711px; height: 400px; overflow: hidden; }
  .banner__backdrop { position: absolute; inset: 0; }

  .banner--gold .banner__backdrop {
    background:
      radial-gradient(ellipse 150px 170px at 40px 330px, rgba(214,188,130,.85), rgba(230,214,180,.35) 60%, transparent 100%),
      radial-gradient(ellipse 130px 150px at 690px 350px, rgba(190,40,40,.75), rgba(225,195,150,.4) 55%, transparent 100%),
      radial-gradient(ellipse 260px 120px at 0 110px, rgba(240,225,195,.7), transparent 100%),
      var(--white);
  }
  .banner--wine .banner__backdrop {
    background: linear-gradient(180deg, var(--plum) 0%, #3a1a2c 30%, var(--wine) 62%, var(--rust) 100%);
  }
  .banner--copper .banner__backdrop {
    background:
      radial-gradient(ellipse 120px 150px at 620px 80px, rgba(165,30,50,.85), rgba(200,120,130,.3) 60%, transparent 100%),
      radial-gradient(ellipse 90px 180px at 20px 290px, rgba(170,25,40,.8), rgba(220,150,150,.3) 60%, transparent 100%),
      radial-gradient(ellipse 100px 60px at 600px 400px, rgba(160,30,50,.7), transparent 100%),
      radial-gradient(ellipse 180px 110px at 60px 40px, rgba(215,195,140,.6), transparent 100%),
      var(--white);
  }

  .banner__sparkles { position: absolute; inset: 0; width: 711px; height: 400px; pointer-events: none; }

  .banner__content { position: absolute; inset: 0; text-align: center; }

  .banner__presenter {
    position: absolute; top: 34px; left: 0; width: 100%;
    font-family: 'Montserrat', sans-serif; font-weight: 500;
    font-size: 15.5px; letter-spacing: 3.4px; padding-left: 3px;
  }
  .banner__presents-rule { position: absolute; top: 56px; left: 212px; width: 290px; height: 20px; }
  .banner__presents {
    position: absolute; top: 47px; left: 0; width: 100%;
    font-family: 'Pinyon Script', cursive; font-size: 21px; letter-spacing: 1px;
  }

  .banner__headline, .banner__script {
    background-clip: text; -webkit-background-clip: text; color: transparent;
    background-size: 3px 3px, 5px 4px, 7px 6px, 100% 100%;
  }
  .banner__headline {
    position: absolute; left: 0; width: 100%;
    font-family: 'Archivo Black', sans-serif; font-size: 40px; line-height: 1;
    letter-spacing: 20px; padding-left: 20px;
  }
  .banner__headline--first { top: 98px; }
  .banner__headline--second { top: 138px; }

  .banner__script {
    position: absolute; top: 160px; left: 0; width: 100%;
    font-family: 'Allura', cursive; font-size: 118px; line-height: 1;
    padding: 0 20px 24px;
  }

  .banner__divider { position: absolute; top: 293px; left: 252px; width: 207px; height: 12px; }
  .banner__date {
    position: absolute; top: 318px; left: 0; width: 100%;
    font-family: 'Montserrat', sans-serif; font-weight: 500;
    font-size: 15.5px; letter-spacing: 2.6px; padding-left: 3px;
  }

  .banner--gold .banner__presenter, .banner--gold .banner__presents, .banner--gold .banner__date { color: var(--gold); }
  .banner--gold .banner__headline, .banner--gold .banner__script,
  .banner--wine .banner__headline, .banner--wine .banner__script {
    background-image:
      radial-gradient(circle at 1px 1px, var(--glint) 0.6px, transparent 1.1px),
      radial-gradient(circle at 2px 3px, var(--grain) 0.7px, transparent 1.2px),
      radial-gradient(circle at 5px 2px, var(--glint) 0.8px, transparent 1.3px),
      linear-gradient(100deg, var(--gold-dark), var(--gold-light) 30%, var(--gold) 55%, var(--gold-light) 80%, var(--gold-dark));
  }
  .banner--wine .banner__presenter, .banner--wine .banner__presents, .banner--wine .banner__date { color: var(--white); }
  .banner--copper .banner__presenter, .banner--copper .banner__presents, .banner--copper .banner__date { color: var(--copper); }
  .banner--copper .banner__headline, .banner--copper .banner__script {
    background-image:
      radial-gradient(circle at 1px 1px, var(--glint) 0.6px, transparent 1.1px),
      radial-gradient(circle at 2px 3px, var(--grain) 0.7px, transparent 1.2px),
      radial-gradient(circle at 5px 2px, var(--glint) 0.8px, transparent 1.3px),
      linear-gradient(100deg, var(--copper-dark), var(--copper-light) 35%, var(--copper) 60%, var(--copper-light) 85%, var(--copper-dark));
  }
  .banner--gold svg { color: var(--gold); }
  .banner--wine svg { color: var(--white); }
  .banner--copper svg { color: var(--copper); }
  .banner__sparkles { color: var(--star) !important; }
</style>
</head>
<body>
<main class="banner-set">

  <section class="banner banner--gold">
    <div class="banner__backdrop" role="img" aria-label="Soft white and gold holiday photo with glitter ornaments on the left and a red gift with ribbon on the right"></div>
    <svg class="banner__sparkles" viewBox="0 0 711 400" aria-hidden="true"><g fill="currentColor"><path d="M16 182l1 9 8 1-8 1-1 9-1-9-8-1 8-1z" opacity=".9"/><path d="M560 328l1 7 6 1-6 1-1 7-1-7-6-1 6-1z" opacity=".9"/></g></svg>
    <div class="banner__content">
      <p class="banner__presenter">CEDAR GATE COMMUNITY CHURCH</p>
      <svg class="banner__presents-rule" viewBox="0 0 290 20" aria-hidden="true"><g stroke="currentColor" stroke-width="1" fill="currentColor"><line x1="4" y1="10" x2="88" y2="10"/><line x1="200" y1="10" x2="286" y2="10"/><path d="M0 10l4-2.5 4 2.5-4 2.5z"/><path d="M282 10l4-2.5 4 2.5-4 2.5z"/></g></svg>
      <p class="banner__presents">presents</p>
      <h1 class="banner__headline banner__headline--first">MARWOOD</h1>
      <p class="banner__headline banner__headline--second">HOLIDAY</p>
      <p class="banner__script">Jubilee</p>
      <svg class="banner__divider" viewBox="0 0 207 12" aria-hidden="true"><g fill="currentColor" stroke="currentColor"><line x1="2" y1="6" x2="85" y2="6" stroke-width="1"/><line x1="122" y1="6" x2="205" y2="6" stroke-width="1"/><circle cx="2.5" cy="6" r="2.2" stroke="none"/><circle cx="204.5" cy="6" r="2.2" stroke="none"/><path d="M103.5 0l1.5 4.5 4.5 1.5-4.5 1.5-1.5 4.5-1.5-4.5-4.5-1.5 4.5-1.5z" stroke="none"/><path d="M93 6l2-2 2 2-2 2z" stroke="none"/><path d="M110 6l2-2 2 2-2 2z" stroke="none"/></g></svg>
      <p class="banner__date">DECEMBER 14 &amp; 15 | 6:00PM</p>
    </div>
  </section>

  <section class="banner banner--wine">
    <div class="banner__backdrop" role="img" aria-label="Deep plum to wine-red gradient with soft bokeh light circles"></div>
    <svg class="banner__sparkles" viewBox="0 0 711 400" aria-hidden="true"><g fill="currentColor"><path d="M108 42l2.2 20 20 2.2-20 2.2-2.2 20-2.2-20-20-2.2 20-2.2z"/><circle cx="108" cy="64" r="4" opacity=".7"/><path d="M225 90l1.8 17 16 1.8-16 1.8-1.8 17-1.8-17-16-1.8 16-1.8z"/><circle cx="225" cy="109" r="3.5" opacity=".7"/><path d="M589 276l1.8 17 16 1.8-16 1.8-1.8 17-1.8-17-16-1.8 16-1.8z"/><circle cx="589" cy="295" r="3.5" opacity=".7"/></g></svg>
    <div class="banner__content">
      <p class="banner__presenter">CEDAR GATE COMMUNITY CHURCH</p>
      <svg class="banner__presents-rule" viewBox="0 0 290 20" aria-hidden="true"><g stroke="currentColor" stroke-width="1" fill="currentColor"><line x1="4" y1="10" x2="88" y2="10"/><line x1="200" y1="10" x2="286" y2="10"/><path d="M0 10l4-2.5 4 2.5-4 2.5z"/><path d="M282 10l4-2.5 4 2.5-4 2.5z"/></g></svg>
      <p class="banner__presents">presents</p>
      <p class="banner__headline banner__headline--first">MARWOOD</p>
      <p class="banner__headline banner__headline--second">HOLIDAY</p>
      <p class="banner__script">Jubilee</p>
      <svg class="banner__divider" viewBox="0 0 207 12" aria-hidden="true"><g fill="currentColor" stroke="currentColor"><line x1="2" y1="6" x2="85" y2="6" stroke-width="1"/><line x1="122" y1="6" x2="205" y2="6" stroke-width="1"/><circle cx="2.5" cy="6" r="2.2" stroke="none"/><circle cx="204.5" cy="6" r="2.2" stroke="none"/><path d="M103.5 0l1.5 4.5 4.5 1.5-4.5 1.5-1.5 4.5-1.5-4.5-4.5-1.5 4.5-1.5z" stroke="none"/><path d="M93 6l2-2 2 2-2 2z" stroke="none"/><path d="M110 6l2-2 2 2-2 2z" stroke="none"/></g></svg>
      <p class="banner__date">DECEMBER 14 &amp; 15 | 6:00PM</p>
    </div>
  </section>

  <section class="banner banner--copper">
    <div class="banner__backdrop" role="img" aria-label="Snowy white holiday photo with red plaid ornaments, berries and pine sprigs at the corners"></div>
    <svg class="banner__sparkles" viewBox="0 0 711 400" aria-hidden="true"><g fill="#e2c27a"><path d="M40 50l1 8 7 1-7 1-1 8-1-8-7-1 7-1z" opacity=".9"/><path d="M660 330l1 7 6 1-6 1-1 7-1-7-6-1 6-1z" opacity=".8"/></g></svg>
    <div class="banner__content">
      <p class="banner__presenter">CEDAR GATE COMMUNITY CHURCH</p>
      <svg class="banner__presents-rule" viewBox="0 0 290 20" aria-hidden="true"><g stroke="currentColor" stroke-width="1" fill="currentColor"><line x1="4" y1="10" x2="88" y2="10"/><line x1="200" y1="10" x2="286" y2="10"/><path d="M0 10l4-2.5 4 2.5-4 2.5z"/><path d="M282 10l4-2.5 4 2.5-4 2.5z"/></g></svg>
      <p class="banner__presents">presents</p>
      <p class="banner__headline banner__headline--first">MARWOOD</p>
      <p class="banner__headline banner__headline--second">HOLIDAY</p>
      <p class="banner__script">Jubilee</p>
      <svg class="banner__divider" viewBox="0 0 207 12" aria-hidden="true"><g fill="currentColor" stroke="currentColor"><line x1="2" y1="6" x2="85" y2="6" stroke-width="1"/><line x1="122" y1="6" x2="205" y2="6" stroke-width="1"/><circle cx="2.5" cy="6" r="2.2" stroke="none"/><circle cx="204.5" cy="6" r="2.2" stroke="none"/><path d="M103.5 0l1.5 4.5 4.5 1.5-4.5 1.5-1.5 4.5-1.5-4.5-4.5-1.5 4.5-1.5z" stroke="none"/><path d="M93 6l2-2 2 2-2 2z" stroke="none"/><path d="M110 6l2-2 2 2-2 2z" stroke="none"/></g></svg>
      <p class="banner__date">DECEMBER 14 &amp; 15 | 6:00PM</p>
    </div>
  </section>

</main>
</body>
</html>
```